Independent IT Consulting Professional. Looking for a clean crisp, somewhat traditional design. I have also attached the initial off-the-shelf design from PrintHaven. My company has grown quickly, and I would like to take the card to the next level. Should be sharp, mature, classy well laid-out and convey confidence. I don't think the off-the-shelf design does this. I like the logo I have for the time being, but if someone has something better in mind, I would be happy to consider an alternative. I would also like to see the color Cyan used in a small way, either with the logo or some other color treatment, as I feel like this is a modern color that I always liked, but never was able to make anything work with it.
Industry/Entity Type
It Company
Contact Information for Business Card
Carter J. Whitlow
Owner
TrellMark Solutions
2817 Ashborough Lane
Manlius, NY 13104
(917) 555-0148
cwhitlow@trellmarksolutions.example
www.trellmarksolutions.example
Tagline: Business Technology Services and Consulting

```html
<!DOCTYPE html>
<html lang="en">
<head>
<meta charset="utf-8">
<title>TrellMark Solutions – Business Card</title>
<link href="https://fonts.googleapis.com/css2?family=Michroma&family=Roboto+Condensed:wght@700&display=swap" rel="stylesheet">
<style>
  :root {
    --backdrop: #8f8f8f;
    --card: #ffffff;
    --card-shade: #eef0f1;
    --ink: #111111;
    --text: #3a3a3a;
    --accent: #2a7cc9;
  }
  * { margin: 0; padding: 0; box-sizing: border-box; }
  html, body {
    width: 1200px; height: 895px; overflow: hidden;
    background: var(--backdrop);
    font-family: "Michroma", "Eurostile", sans-serif;
  }
  .card {
    position: absolute;
    width: 560px; height: 320px;
    background: linear-gradient(160deg, var(--card) 60%, var(--card-shade));
    box-shadow: 0 10px 24px rgba(0,0,0,.35);
    overflow: hidden;
  }
  .card--front { left: 600px; top: 110px; }
  .card--back  { left: 40px;  top: 460px; }
  .card__bands { position: absolute; inset: 0; }

  .brand {
    position: absolute;
    color: var(--ink);
    font-family: "Roboto Condensed", "Arial Narrow", sans-serif;
    font-weight: 700;
    line-height: 1.05;
    display: flex; align-items: center; gap: 10px;
  }
  .brand__mark { width: 14px; height: 14px; background: var(--accent); flex: none; }
  .card--front .brand { left: 50%; top: 50%; transform: translate(-50%, -50%); font-size: 40px; }
  .card--front .brand__mark { width: 22px; height: 22px; }
  .card--back .brand { left: 26px; top: 22px; font-size: 26px; }

  .holder { position: absolute; left: 284px; top: 68px; color: var(--text); }
  .holder__name { font-size: 15px; letter-spacing: 1px; text-transform: uppercase; white-space: nowrap; }
  .holder__role { font-size: 7px; letter-spacing: 1px; margin-top: 8px; text-transform: uppercase; }

  .contact { position: absolute; top: 184px; color: var(--text); line-height: 1.8; white-space: nowrap; }
  .contact--web { left: 16px; width: 176px; font-size: 6px; }
  .contact--address { left: 210px; width: 160px; font-size: 9px; }
  .contact--phone { left: 392px; font-size: 11px; letter-spacing: .5px; line-height: 1.6; }
</style>
</head>
<body>

<section class="card card--front" aria-label="Card front">
  <svg class="card__bands" viewBox="0 0 560 320" aria-hidden="true">
    <rect x="0" y="0" width="560" height="44" fill="#111"/>
    <rect x="0" y="276" width="560" height="44" fill="#111"/>
    <polygon points="150,0 160,0 174,22 160,44 150,44 164,22" fill="#fff"/>
    <polygon points="420,0 430,0 444,22 430,44 420,44 434,22" fill="#fff"/>
    <polygon points="110,276 120,276 134,298 120,320 110,320 124,298" fill="#fff"/>
    <polygon points="370,276 380,276 394,298 380,320 370,320 384,298" fill="#fff"/>
  </svg>
  <div class="brand"><span class="brand__mark"></span><span>TrellMark<br>Solutions</span></div>
</section>

<section class="card card--back" aria-label="Card back">
  <svg class="card__bands" viewBox="0 0 560 320" aria-hidden="true">
    <rect x="0" y="124" width="560" height="40" fill="#111"/>
    <rect x="0" y="282" width="560" height="38" fill="#111"/>
    <polygon points="190,124 200,124 214,144 200,164 190,164 204,144" fill="#fff"/>
    <polygon points="372,124 382,124 396,144 382,164 372,164 386,144" fill="#fff"/>
    <polygon points="150,282 160,282 174,301 160,320 150,320 164,301" fill="#fff"/>
    <polygon points="420,282 430,282 444,301 430,320 420,320 434,301" fill="#fff"/>
    <g class="icon-web" fill="none" stroke="#2a7cc9" stroke-width="1.6">
      <circle cx="92" cy="144" r="9"/>
      <ellipse cx="92" cy="144" rx="4" ry="9"/>
      <line x1="83" y1="144" x2="101" y2="144"/>
      <line x1="85" y1="139" x2="99" y2="139"/>
      <line x1="85" y1="149" x2="99" y2="149"/>
    </g>
    <path class="icon-pin" d="M290 134a7 7 0 0 1 7 7c0 5-7 13-7 13s-7-8-7-13a7 7 0 0 1 7-7z" fill="#2a7cc9"/>
    <circle cx="290" cy="141" r="2.4" fill="#111"/>
    <g class="icon-phone">
      <rect x="468" y="133" width="12" height="22" rx="2" fill="none" stroke="#2a7cc9" stroke-width="1.6"/>
      <line x1="472" y1="151" x2="476" y2="151" stroke="#2a7cc9" stroke-width="1.6"/>
    </g>
  </svg>

  <div class="brand"><span class="brand__mark"></span><span>TrellMark<br>Solutions</span></div>

  <div class="holder">
    <p class="holder__name">Carter J. Whitlow</p>
    <p class="holder__role">Owner</p>
  </div>

  <div class="contact contact--web">
    <p>cwhitlow@trellmarksolutions.example</p>
    <p>www.trellmarksolutions.example</p>
  </div>
  <div class="contact contact--address">
    <p>2817 Ashborough Lane</p>
    <p>Manlius, NY 13104</p>
  </div>
  <div class="contact contact--phone">
    <p>(917) 555-0148</p>
    <p>(917) 555-0148</p>
  </div>
</section>

</body>
</html>
```